Plakat-Design für Werbetafel-Design für Fussballplatz
Zielgruppe
IT Consulting Dienstleistungen für Internationale Kunden
Aufgabenstellung
Werbetafel-Design für Fussballplatz. (Logo in groß + Slogan 'THE CODE STEWARDS')
Format: 3,0 x 0,75 m
Druckdatenvorabe anbei.

```html
<!DOCTYPE html>
<html lang="en">
<head>
<meta charset="utf-8">
<title>NORVANTIS – Pitch Boundary Board</title>
<link rel="stylesheet" href="https://fonts.googleapis.com/css2?family=Lato:wght@300;400&display=swap">
<style>
  :root {
    --brand-blue: #0095d5;
    --brand-green: #87a92b;
    --ink: #1d1d1b;
    --paper: #ffffff;
    --frame: #1d1d1b;
  }
  html, body {
    margin: 0;
    padding: 0;
    width: 1200px;
    height: 600px;
    overflow: hidden;
    background: var(--paper);
  }
  .canvas {
    position: relative;
    width: 1200px;
    height: 600px;
  }
  .board {
    position: absolute;
    left: 0;
    top: 150px;
    width: 1198px;
    height: 298px;
    border: 1px solid var(--frame);
    background: var(--paper);
    overflow: hidden;
  }
  .brand-square {
    position: absolute;
    left: 150px;
    top: 86px;
    width: 64px;
    height: 64px;
    background: var(--brand-blue);
  }
  .brand-name {
    position: absolute;
    left: 250px;
    top: 68px;
    margin: 0;
    font-family: "Lato", sans-serif;
    font-weight: 400;
    font-size: 84px;
    line-height: 1;
    letter-spacing: 1px;
    color: var(--ink);
  }
  .slogan {
    position: absolute;
    left: 370px;
    top: 198px;
    width: 576px;
    height: 65px;
    margin: 0;
    background: var(--brand-green);
    color: var(--paper);
    font-family: "Lato", sans-serif;
    font-weight: 300;
    font-size: 46px;
    line-height: 65px;
    text-align: center;
    letter-spacing: 0.5px;
  }
  .corner-decor {
    position: absolute;
    right: 0;
    top: 0;
    width: 274px;
    height: 170px;
    background: linear-gradient(225deg, rgba(0,149,213,0.55) 0%, rgba(135,169,43,0.35) 55%, rgba(255,255,255,0) 100%);
  }
</style>
</head>
<body>
  <main class="canvas">
    <section class="board">
      <div class="brand-square"></div>
      <h1 class="brand-name">NORVANTIS</h1>
      <p class="slogan">THE CODE STEWARDS</p>
      <div class="corner-decor" role="img" aria-label="Decorative scatter of blue and green pixel squares in the top right corner"></div>
    </section>
  </main>
</body>
</html>
```